RW Frameworks Inc Business cards

We need business cards using our existing logo but slightly modified. Right now the logo says RW Framework Masonry. We want to keep the RW part of the design, but replace the Framework Masonry portion with "FRAMEWORKS". Please see the attached file.
Ideally this would be a blank template so we can add Different Names, titles, and phone numbers later.
On the one side we want only the logo and on the other side the detail. I'm attaching an example for you to see.
Please reach out with any other questions. Our address and other details will be given out once we find a design we like.

Target Market(s)

Construction Industry

```html
<!DOCTYPE html>
<html lang="en">
<head>
<meta charset="utf-8">
<title>RW Frameworks – Business Cards</title>
<link rel="stylesheet" href="https://fonts.googleapis.com/css2?family=Oswald:wght@500&family=Roboto:wght@400;700&family=Roboto+Condensed:wght@400&display=swap">
<style>
  :root {
    --bg: #dde9f2;
    --brand-blue: #1e76bd;
    --brand-grey: #808083;
    --silver: #c8c9cb;
    --silver-light: #d9dbde;
    --ink: #1d1d1f;
    --white: #ffffff;
  }
  * { margin: 0; padding: 0; box-sizing: border-box; }
  html, body {
    width: 1200px; height: 1200px; overflow: hidden;
    background: var(--bg);
    font-family: "Roboto", Arial, sans-serif;
  }
  .canvas { position: relative; width: 1200px; height: 1200px; }
  .card {
    position: absolute; left: 283px; width: 634px; height: 362px; overflow: hidden;
  }
  .card--front { top: 174px; background: var(--white); }
  .card--back { top: 609px; background: var(--brand-blue); }

  .brand { position: absolute; }
  .brand__mark {
    display: block; font-weight: 700; line-height: 1; letter-spacing: 2px;
  }
  .brand__tagline {
    display: block; font-family: "Roboto Condensed", Arial, sans-serif;
    white-space: nowrap;
  }
  .card--front .brand { left: 35px; top: 28px; width: 206px; }
  .card--front .brand__mark { font-size: 96px; color: var(--brand-blue); }
  .card--front .brand__tagline {
    margin-top: 4px; font-size: 17px; letter-spacing: 10.2px; color: var(--brand-grey);
  }
  .card--back .brand { left: 171px; top: 100px; width: 292px; text-align: center; }
  .card--back .brand__mark { font-size: 128px; color: var(--silver); }
  .card--back .brand__tagline {
    margin-top: 12px; font-size: 24px; letter-spacing: 14.4px; padding-left: 14.4px;
    color: var(--silver-light);
  }

  .person { position: absolute; right: 26px; top: 175px; text-align: right; }
  .person__name {
    font-family: "Oswald", "Arial Narrow", sans-serif; font-weight: 500;
    font-size: 26px; line-height: 28px; color: var(--brand-blue); letter-spacing: -0.3px;
  }
  .person__title { font-size: 15px; line-height: 18px; color: var(--ink); }
  .person-bar {
    position: absolute; right: 0; top: 175px; width: 20px; height: 43px;
    background: var(--brand-blue);
  }

  .contact { position: absolute; left: 35px; top: 236px; list-style: none; }
  .contact__item {
    display: flex; align-items: center; gap: 9px;
    font-size: 16.5px; line-height: 20px; color: var(--ink);
  }
  .contact__icon { width: 11px; height: 11px; fill: var(--brand-blue); flex: none; }

  .footer-wave { position: absolute; left: 0; top: 0; width: 634px; height: 362px; }
  .website {
    position: absolute; left: 35px; top: 328px;
    font-size: 16px; color: var(--white);
  }
</style>
</head>
<body>
<main class="canvas">
  <section class="card card--front" aria-label="Business card front">
    <div class="brand">
      <span class="brand__mark">RW</span>
      <span class="brand__tagline">FRAMEWORKS</span>
    </div>

    <div class="person">
      <p class="person__name">DANA MERCER</p>
      <p class="person__title">Owner</p>
    </div>
    <div class="person-bar"></div>

    <ul class="contact">
      <li class="contact__item">
        <svg class="contact__icon" viewBox="0 0 24 24" aria-hidden="true"><path d="M6.6 10.8a15.1 15.1 0 0 0 6.6 6.6l2.2-2.2a1 1 0 0 1 1-.25 11.4 11.4 0 0 0 3.6.57 1 1 0 0 1 1 1V20a1 1 0 0 1-1 1A17 17 0 0 1 3 4a1 1 0 0 1 1-1h3.5a1 1 0 0 1 1 1c0 1.250.2 2.450.57 3.57a1 1 0 0 1-.25 1z"/></svg>
        +1 555 010 2040
      </li>
      <li class="contact__item">
        <svg class="contact__icon" viewBox="0 0 24 24" aria-hidden="true"><path d="M2 5h20v14H2z M4 7v.5l8 5.5 8-5.5V7z" fill-rule="evenodd"/></svg>
        dmercer@rwfw.com
      </li>
    </ul>

    <svg class="footer-wave" viewBox="0 0 634 362" aria-hidden="true">
      <path d="M35 308 C 200 294 440 298 598 362 C 440 304 200 302 35 308 Z" fill="var(--brand-grey)"/>
      <path d="M0 314 C 160 302 420 306 596 362 L0 362 Z" fill="var(--brand-blue)"/>
    </svg>
    <p class="website">www.rwfw.com</p>
  </section>

  <section class="card card--back" aria-label="Business card back">
    <div class="brand">
      <span class="brand__mark">RW</span>
      <span class="brand__tagline">FRAMEWORKS</span>
    </div>
  </section>
</main>
</body>
</html>
```